Brightfold Partners Website

Brightfold Partners (BP) provide Analytics & Enterprise Performance Management (EPM) advisory & consultancy services. We are passionate about data and making a difference for our clients by working in partnership with them, helping them on their journey to becoming an Brightfold Partner. We deliver insights which give our clients a competitive edge and a much deeper understanding of their organisation.

We need a website which shows who we are, what we do and how we do it.

www.brightfold-partners.example is our very basic website at the moment. We want to completely revamp it with a corporate look

```html
<!DOCTYPE html>
<html lang="en">
<head>
<meta charset="utf-8">
<title>Brightfold Partners</title>
<link href="https://fonts.googleapis.com/css2?family=Raleway:wght@400;500;600;700&family=Nunito:wght@400;600;700;800&display=swap" rel="stylesheet">
<style>
:root{
  --navy:#0e3d5c;
  --navy-deep:#0a2c44;
  --slate:#2f5872;
  --steel:#3b6d8f;
  --ink:#1f2d3a;
  --text:#3c4650;
  --muted:#6a7784;
  --sky:#2f8fd1;
  --orange:#f0a318;
  --line:#d7dde3;
  --white:#ffffff;
}
*{box-sizing:border-box;margin:0;padding:0}
html,body{width:1200px;height:3919px;overflow:hidden}
body{font-family:"Nunito",sans-serif;color:var(--text);background:var(--white);position:relative}
section,header,footer{position:absolute;left:0;width:1200px;overflow:hidden}
.abs{position:absolute}
h1,h2,h3{font-family:"Raleway",sans-serif;font-weight:500}

/* header */
.site-header{top:0;height:78px;background:var(--white)}
.brand{position:absolute;left:131px;top:14px;display:flex;align-items:center;gap:12px}
.brand-dot{width:46px;height:46px;border-radius:50%;background:var(--slate)}
.brand-name{font-family:"Nunito",sans-serif;font-weight:800;font-size:19px;line-height:22px;letter-spacing:.5px;color:var(--slate);text-transform:uppercase}
.nav{position:absolute;top:31px;font-size:12px;color:var(--ink);font-weight:600;letter-spacing:.3px}
.nav.active{color:var(--steel)}
.hotline{position:absolute;left:941px;top:26px;display:flex;gap:8px;align-items:center}
.hotline small{display:block;font-size:9px;color:var(--muted)}
.hotline strong{display:block;font-size:11px;color:var(--steel);font-weight:700}

/* hero */
.hero{top:78px;height:454px}
.hero-bg{position:absolute;inset:0;background:linear-gradient(100deg,#2a3a44 0%,#1f3745 30%,#163446 55%,#113142 100%)}
.hero-photo{position:absolute;left:0;top:0;width:560px;height:454px;background:radial-gradient(ellipse at 60% 40%,rgba(140,150,160,.45),rgba(20,40,55,0) 70%)}
.hero-kicker{left:614px;top:140px;font-size:14px;color:#e6edf2}
.hero-title{font-family:"Nunito",sans-serif;font-weight:800;font-size:35px;line-height:40px;color:var(--white);text-transform:uppercase}
.btn{position:absolute;display:flex;align-items:center;height:40px;border-radius:20px;font-family:"Nunito",sans-serif;font-weight:700;font-size:11px;color:var(--white);text-transform:uppercase;letter-spacing:.3px}
.btn .btn-dot{width:40px;height:40px;border-radius:50%;background:var(--white);margin-right:14px;border:6px solid currentColor}
.btn-light{background:#3d6883}
.btn-light .btn-dot{border-color:#3d6883}
.btn-dark{background:var(--slate)}
.btn-dark .btn-dot{border-color:var(--slate)}

/* welcome */
.welcome{top:532px;height:577px;background:var(--white)}
.eyebrow{font-family:"Raleway",sans-serif;font-size:16px;color:var(--ink)}
.heading{font-size:35px;line-height:40px;color:var(--slate)}
.body-copy{font-size:12.5px;line-height:20px;color:var(--text)}
.welcome-photo{position:absolute;left:610px;top:74px;width:460px;height:430px;border-radius:50%;background:linear-gradient(135deg,#d9a463 0%,#a7a49c 40%,#5f7384 75%,#2c4556 100%)}

/* services */
.services{top:1109px;height:602px;background:linear-gradient(135deg,#0e3d5c 0%,#0f4262 60%,#0c3654 100%)}
.services .eyebrow,.services .heading,.services .body-copy{color:var(--white)}
.service-card{position:absolute;top:193px;width:300px;height:351px;border-radius:10px;overflow:hidden}
.service-card .label{position:absolute;left:26px;bottom:56px;font-family:"Raleway",sans-serif;font-size:16px;color:var(--white);font-weight:500}
.service-card .icon{position:absolute;left:26px;bottom:88px}
.feature-box{position:absolute;left:27px;top:143px;width:245px;height:167px;background:var(--white);border-radius:8px;padding:20px 14px}
.feature-box h3{font-size:16px;color:var(--ink);margin:46px 0 10px;font-weight:600}
.feature-box p{font-size:10.5px;line-height:17px;color:var(--text)}

/* who */
.who{top:1711px;height:624px;background:var(--white)}
.stat-box{position:absolute;top:330px;width:208px;height:88px;border:1px solid var(--line);padding:14px 12px 0 50px}
.stat-box h3{font-family:"Nunito",sans-serif;font-size:12px;color:var(--ink);font-weight:600}
.stat-box p{font-size:10px;line-height:14px;color:var(--text);margin-top:4px}
.stat-box svg{position:absolute;left:10px;top:16px}

/* how */
.how{top:2335px;height:424px}
.how-bg{position:absolute;inset:0;background:linear-gradient(180deg,#0d2f45 0%,#153a52 55%,#1c4058 100%)}
.center{left:0;width:1200px;text-align:center}
.step{position:absolute;top:190px;width:290px;text-align:center;color:var(--white)}
.step h3{font-size:19px;margin-top:22px;color:var(--white)}
.step p{font-size:11.5px;line-height:19px;color:#c9d6e0;margin-top:8px}

/* contact */
.contact{top:2759px;height:376px;background:var(--white)}
.field{position:absolute;border:1px solid #3a4650;background:var(--white);font-size:10.5px;color:var(--ink);padding:13px 11px}
.submit{position:absolute;left:605px;top:265px;width:318px;height:41px;background:var(--steel);color:var(--white);font-size:11.5px;font-weight:700;letter-spacing:.5px;text-align:center;line-height:41px}

/* cta */
.cta{top:3135px;height:397px}
.cta-bg{position:absolute;inset:0;background:linear-gradient(90deg,#3b4a55 0%,#2b3f4e 40%,#1e3444 70%,#223747 100%)}
.cta .eyebrow{color:var(--white);font-size:20px}
.cta-title{font-size:35px;line-height:38px;color:var(--white)}
.cta-line{font-size:13.5px;color:var(--white);letter-spacing:.3px}
.btn-orange{background:var(--orange)}
.btn-orange .btn-dot{border-color:var(--orange)}
.btn-blue{background:var(--sky)}
.btn-blue .btn-dot{border-color:var(--sky)}

/* footer */
.site-footer{top:3532px;height:387px;background:var(--slate);color:var(--white)}
.site-footer .brand-name{color:var(--white)}
.site-footer .brand-dot{background:var(--white)}
.foot-title{position:absolute;top:66px;font-family:"Raleway",sans-serif;font-size:16px;color:var(--white)}
.foot-link{position:absolute;font-size:11px;color:#e3ebf1;padding-left:12px}
.foot-link::before{content:"";position:absolute;left:0;top:4px;width:6px;height:6px;border-radius:50%;background:var(--sky)}
.foot-contact{position:absolute;left:846px;display:flex;align-items:center;gap:10px;font-size:11px;line-height:13px;color:#e3ebf1}
.foot-contact .ring{width:28px;height:28px;border-radius:50%;border:1.5px solid var(--white);flex:none;display:flex;align-items:center;justify-content:center}
.social{position:absolute;top:244px;width:32px;height:32px;border-radius:50%;background:#4a7390}
.copyright{position:absolute;left:0;width:1200px;top:340px;text-align:center;font-size:9.5px;color:#dfe7ee}
.copyright span{color:var(--sky)}
</style>
</head>
<body>

<header class="site-header">
  <div class="brand"><span class="brand-dot"></span><span class="brand-name">Brightfold<br>Partners</span></div>
  <span class="nav active" style="left:563px">HOME</span>
  <span class="nav" style="left:642px">ABOUT US</span>
  <span class="nav" style="left:744px">SERVICES</span>
  <span class="nav" style="left:841px">CONTACT US</span>
  <div class="hotline">
    <svg width="20" height="20" viewBox="0 0 20 20" fill="none" stroke="#3b6d8f" stroke-width="1.6"><path d="M4 11V9a6 6 0 0 1 12 0v2"/><rect x="2.5" y="10" width="3.5" height="6" rx="1"/><rect x="14" y="10" width="3.5" height="6" rx="1"/></svg>
    <div><small>Have Any Questions?</small><strong>+ 44 1800 555 014</strong></div>
  </div>
</header>

<section class="hero">
  <div class="hero-bg" role="img" aria-label="Presenter pointing at an analytics dashboard with charts"></div>
  <div class="hero-photo"></div>
  <div class="abs hero-kicker">Brightfold Partners</div>
  <h1 class="abs hero-title" style="left:614px;top:160px">Data Analytics &amp;<br>EPM Consulting Services</h1>
  <div class="btn btn-light" style="left:611px;top:269px;width:159px"><span class="btn-dot"></span>Explore More</div>
</section>

<section class="welcome">
  <div class="abs eyebrow" style="left:131px;top:175px">Welcome To</div>
  <h2 class="abs heading" style="left:131px;top:198px">Brightfold Partners</h2>
  <p class="abs body-copy" style="left:131px;top:267px;width:420px">BP are a Data Analytics &amp; EPM company, specialising in the implementation and support of Business Intelligence, EPM and Data Analytics business solutions, both in the Cloud and on-premise.</p>
  <div class="btn btn-dark" style="left:131px;top:357px;width:147px"><span class="btn-dot"></span>Read More</div>
  <div class="welcome-photo" role="img" aria-label="Two consultants reviewing a tablet together"></div>
</section>

<section class="services">
  <div class="abs eyebrow" style="left:131px;top:56px">What We Do</div>
  <h2 class="abs heading" style="left:131px;top:78px;color:#fff">We Offer Consulting<br>Services</h2>
  <p class="abs body-copy" style="left:610px;top:84px;width:440px;color:#fff">Sed ut perspiciatis unde omnis iste natus error sit voluptatem accusantium doloremque laudantium, totam rem aperiam, eaque ipsa quae ab illo inventore veritatis et quasi architecto...</p>

  <div class="service-card" style="left:131px;background:linear-gradient(160deg,#2b3b48,#1a2631 60%,#343c44)" role="img" aria-label="Engineer pointing at building plans on a monitor">
    <svg class="icon" width="40" height="40" viewBox="0 0 40 40" fill="none" stroke="#fff" stroke-width="1.6"><rect x="4" y="4" width="22" height="18"/><path d="M8 10h14M8 15h10"/><circle cx="28" cy="26" r="5"/><path d="M20 38c1-6 4-8 8-8s7 2 8 8"/></svg>
    <div class="label">Advise &amp; Architect Services</div>
  </div>
  <div class="service-card" style="left:450px;background:linear-gradient(170deg,#6c94b4,#3c6d95 60%,#2f5f88)" role="img" aria-label="Consultant working at a desk">
    <div class="feature-box">
      <svg class="abs" style="left:14px;top:16px" width="44" height="44" viewBox="0 0 44 44" fill="none" stroke="#1f4e6e" stroke-width="1.6"><rect x="4" y="6" width="12" height="12" rx="2"/><rect x="18" y="16" width="22" height="18" rx="3"/><path d="M24 34l-4 6v-6M22 24h14M22 28h10"/><path d="M10 18v8h8"/></svg>
      <h3>Design &amp; Implement</h3>
      <p>Working with the project management team, through each stage of the project, with clearly defined deliverables...</p>
    </div>
  </div>
  <div class="service-card" style="left:770px;background:linear-gradient(160deg,#c7b59a,#8a7a66 55%,#bfa98a)" role="img" aria-label="Two colleagues reviewing documents at a table">
    <svg class="icon" width="40" height="40" viewBox="0 0 40 40" fill="none" stroke="#fff" stroke-width="1.6"><circle cx="20" cy="14" r="9"/><circle cx="20" cy="14" r="4"/><path d="M6 34c6-6 14-6 18-2l10-4"/></svg>
    <div class="label">Optimise &amp; Manage</div>
  </div>
</section>

<section class="who">
  <svg class="abs" style="left:91px;top:70px" width="510" height="470" viewBox="0 0 510 470" role="img" aria-label="Collage of business professionals in diamond frames">
    <defs>
      <linearGradient id="d1" x1="0" y1="0" x2="1" y2="1"><stop offset="0" stop-color="#2e8a7e"/><stop offset="1" stop-color="#1f3040"/></linearGradient>
      <linearGradient id="d2" x1="0" y1="0" x2="1" y2="1"><stop offset="0" stop-color="#4b4440"/><stop offset="1" stop-color="#1b2430"/></linearGradient>
      <linearGradient id="d3" x1="0" y1="0" x2="1" y2="1"><stop offset="0" stop-color="#c5d5e6"/><stop offset="1" stop-color="#7f9ab8"/></linearGradient>
      <linearGradient id="d4" x1="0" y1="0" x2="1" y2="1"><stop offset="0" stop-color="#d2d6da"/><stop offset="1" stop-color="#3a4652"/></linearGradient>
    </defs>
    <polygon points="260,8 372,120 260,232 148,120" fill="url(#d1)"/>
    <polygon points="148,130 252,234 148,338 44,234" fill="url(#d2)"/>
    <polygon points="372,130 476,234 372,338 268,234" fill="url(#d3)"/>
    <polygon points="260,244 364,348 260,452 156,348" fill="url(#d4)"/>
  </svg>
  <div class="abs eyebrow" style="left:642px;top:140px">Company</div>
  <h2 class="abs heading" style="left:642px;top:162px">Who We Are</h2>
  <p class="abs body-copy" style="left:642px;top:228px;width:432px">Sed ut perspiciatis unde omnis iste natus error sit voluptatem accusantium doloremque laudantium, totam rem aperiam, eaque ipsa quae ab illo inventore veritatis et quasi architecto beatae vitae dicta sunt explicabo.</p>
  <div class="stat-box" style="left:642px">
    <svg width="36" height="30" viewBox="0 0 36 30" fill="none" stroke="#3b6d8f" stroke-width="1.5"><circle cx="18" cy="8" r="4"/><circle cx="6" cy="16" r="3"/><circle cx="30" cy="16" r="3"/><path d="M10 28c1-6 4-9 8-9s7 3 8 9"/></svg>
    <h3>Experience</h3><p>Our great team of more than 1400 software experts.</p>
  </div>
  <div class="stat-box" style="left:862px">
    <svg width="26" height="26" viewBox="0 0 26 26" fill="#3b6d8f"><circle cx="13" cy="8" r="6"/><path d="M2 26c1-8 5-11 11-11s10 3 11 11z"/></svg>
    <h3>Quick Support</h3><p>We'll help you test bold new ideas while sharing your.</p>
  </div>
  <div class="btn btn-dark" style="left:642px;top:446px;width:148px"><span class="btn-dot"></span>Read More</div>
</section>

<section class="how">
  <div class="how-bg" role="img" aria-label="Team meeting in a dimly lit office"></div>
  <h2 class="abs center" style="top:78px;font-size:33px;color:#fff">How We Do It</h2>
  <p class="abs center" style="top:126px;font-size:12.5px;color:#e0e8ee">Sed ut perspiciatis unde omnis iste natus error sit voluptatem</p>
  <svg class="abs" style="left:403px;top:207px" width="74" height="10" viewBox="0 0 74 10"><path d="M0 5h68" stroke="#3f9bd8" stroke-width="1.5"/><path d="M66 1l6 4-6 4" fill="#3f9bd8"/></svg>
  <svg class="abs" style="left:722px;top:207px" width="74" height="10" viewBox="0 0 74 10"><path d="M0 5h68" stroke="#3f9bd8" stroke-width="1.5"/><path d="M66 1l6 4-6 4" fill="#3f9bd8"/></svg>
  <div class="step" style="left:135px">
    <svg width="72" height="56" viewBox="0 0 72 56" fill="none" stroke="#fff" stroke-width="2"><path d="M6 48V18l8 10V14l8 18V10l8 22V18l8 14V24M2 48h50"/><path d="M8 10l50 40" stroke="#3f9bd8"/></svg>
    <h3>Eiusmod Tempor</h3><p>Sed ut perspiciatis unde omnis iste natus error sit voluptatem accusantium</p>
  </div>
  <div class="step" style="left:454px">
    <svg width="60" height="56" viewBox="0 0 60 56" fill="none" stroke="#fff" stroke-width="1.8"><rect x="4" y="4" width="24" height="14"/><circle cx="16" cy="30" r="6"/><path d="M4 54c1-10 6-14 12-14s11 4 12 14"/><circle cx="42" cy="14" r="7" stroke="#3f9bd8"/><path d="M32 36c1-8 5-12 10-12s9 4 10 12"/></svg>
    <h3>Tempora Incidunt</h3><p>Sed ut perspiciatis unde omnis iste natus error sit voluptatem accusantium</p>
  </div>
  <div class="step" style="left:775px">
    <svg width="64" height="56" viewBox="0 0 64 56" fill="none" stroke="#fff" stroke-width="1.8"><circle cx="22" cy="20" r="14"/><ellipse cx="22" cy="20" rx="6" ry="14"/><path d="M8 20h28"/><path d="M34 26h24v16H44l-6 6v-6h-4z" stroke="#3f9bd8"/></svg>
    <h3>Finibus Bonorum</h3><p>Sed ut perspiciatis unde omnis iste natus error sit voluptatem accusantium</p>
  </div>
</section>

<section class="contact">
  <h2 class="abs center" style="top:62px;font-size:33px;color:var(--slate)">Contact Us</h2>
  <p class="abs center" style="top:110px;font-size:12.5px;color:var(--text)">Sed ut perspiciatis unde omnis iste natus error sit voluptatem</p>
  <div class="field" style="left:277px;top:157px;width:318px;height:41px">Name:</div>
  <div class="field" style="left:277px;top:210px;width:318px;height:41px">Email:</div>
  <div class="field" style="left:277px;top:265px;width:318px;height:41px">Phone:</div>
  <div class="field" style="left:605px;top:157px;width:318px;height:95px">Message:</div>
  <div class="submit">SUBMIT</div>
</section>

<section class="cta">
  <div class="cta-bg" role="img" aria-label="Business people in conversation"></div>
  <svg class="abs" style="left:290px;top:0" width="340" height="397" viewBox="0 0 340 397"><polygon points="30,0 170,0 330,200 170,397 40,397 180,200" fill="#1f5bd0" opacity=".85"/></svg>
  <div class="abs eyebrow" style="left:669px;top:64px">Contact Us To</div>
  <h2 class="abs cta-title" style="left:669px;top:91px">Discuss Your Business<br>Needs</h2>
  <p class="abs cta-line" style="left:669px;top:172px">Advise &amp; Architect &nbsp;|&nbsp; Design &amp; Implement &nbsp;|&nbsp; Optimise &amp; Manage</p>
  <div class="btn btn-orange" style="left:671px;top:230px;width:146px"><span class="btn-dot"></span>01 555 0142</div>
  <div class="btn btn-blue" style="left:833px;top:230px;width:145px"><span class="btn-dot"></span>Contact Us</div>
</section>

<footer class="site-footer">
  <div class="brand" style="top:72px"><span class="brand-dot"></span><span class="brand-name">Brightfold<br>Partners</span></div>
  <p class="abs" style="left:131px;top:150px;width:230px;font-size:11px;line-height:19px;color:#e3ebf1">Brightfold Partners is an exciting start-up in the Data Analytics and EPM space.</p>
  <span class="social" style="left:131px"></span>
  <span class="social" style="left:172px"></span>

  <div class="foot-title" style="left:462px">Quick Links</div>
  <div class="foot-link" style="left:462px;top:107px">Home</div>
  <div class="foot-link" style="left:462px;top:131px">About Us</div>
  <div class="foot-link" style="left:462px;top:156px">Services</div>
  <div class="foot-link" style="left:462px;top:180px">Contact Us</div>

  <div class="foot-title" style="left:636px">Services</div>
  <div class="foot-link" style="left:636px;top:107px">Advise &amp; Architect</div>
  <div class="foot-link" style="left:636px;top:131px">Design &amp; Implement</div>
  <div class="foot-link" style="left:636px;top:156px">Optimse &amp; Manage</div>

  <div class="foot-title" style="left:846px">Contact Us</div>
  <div class="foot-contact" style="top:112px">
    <span class="ring"><svg width="12" height="14" viewBox="0 0 12 14" fill="#fff"><path d="M6 0a5 5 0 0 1 5 5c0 4-5 9-5 9S1 9 1 5a5 5 0 0 1 5-5zm0 3a2 2 0 1 0 0 4 2 2 0 0 0 0-4z"/></svg></span>
    <span>12 Harbour Lane, Northfield,<br>Dublin 4, D04 QX11</span>
  </div>
  <div class="foot-contact" style="top:162px">
    <span class="ring"><svg width="12" height="12" viewBox="0 0 12 12" fill="#fff"><path d="M2 0l2 3-1 1.5c1 2 2.5 3.5 4.5 4.5L9 8l3 2-1.5 2C5 12 0 7 0 1.5z"/></svg></span>
    <span>01 555 0142</span>
  </div>
  <div class="foot-contact" style="top:213px">
    <span class="ring"><svg width="13" height="10" viewBox="0 0 13 10" fill="none" stroke="#fff" stroke-width="1.3"><rect x=".5" y=".5" width="12" height="9"/><path d="M.5 .5l6 5 6-5"/></svg></span>
    <span>info@brightfold-partners.example</span>
  </div>

  <div class="abs" style="left:131px;top:289px;width:940px;height:1px;background:rgba(255,255,255,.25)"></div>
  <div class="copyright">Copyright © 2022 <span>Northwind Studio</span>. All Rights Reserved.</div>
</footer>

</body>
</html>
```